Velmoro Consulting Business

** Please add the content information from my old business card
1. I would like to see a two sided business card with both options with the 1st Option--Sketch Nest-new WHITE BACKGROUND LOGO
2 nd Option-Sketch Nest - new BLACK- Background Logo
3rd -Option a business card with my Photo on the card
Please add the new word to the card information:
EXECUTION
AS THE OWNER'S REP
WE AIM TO ACHIEVE YOUR
INFRASTRUCTURE VISION with
OUR SPECIALIZATION & EXECUTION in:

FUNDING Planning
BUSINESS Planning
INFRASTRUCTURE Planning
PROJECT Management
Since 2012
_____________________________________________________________________
I want to get spot uv raised printing. I was liking a a nice rich white linen paper stock with black writing & NOT A COLORED CARD other than a variety of white or black cards concept

```html
<!DOCTYPE html>
<html lang="en">
<head>
<meta charset="utf-8">
<title>Velmoro Consulting – Business Cards</title>
<link rel="stylesheet" href="https://fonts.googleapis.com/css2?family=Montserrat:wght@400;500;600;700;800&display=swap">
<style>
  :root {
    --stage: #2e2e2e;
    --card-black: #050505;
    --card-white: #ffffff;
    --brand-red: #e3163b;
    --ink: #1a1a1a;
    --ink-soft: #2b2b2b;
    --paper-text: #ffffff;
  }
  * { box-sizing: border-box; margin: 0; padding: 0; }
  html, body {
    width: 1200px; height: 689px; overflow: hidden;
    background: var(--stage);
    font-family: "Montserrat", Arial, sans-serif;
  }
  .stage {
    position: relative; width: 1200px; height: 689px;
  }
  .card {
    position: absolute; top: 190px;
    width: 540px; height: 310px;
    border-radius: 22px; overflow: hidden;
  }

  /* ---------- Back: black side ---------- */
  .card--back { left: 40px; background: var(--card-black); color: var(--paper-text); }
  .back-brand {
    position: absolute; left: 42px; top: 118px; width: 210px;
  }
  .brand-row { display: flex; align-items: center; gap: 8px; }
  .brand-mark {
    width: 12px; height: 12px; background: var(--brand-red); flex: none;
  }
  .brand-name {
    font-weight: 700; font-size: 40px; line-height: 1; letter-spacing: -0.5px;
  }
  .brand-sub {
    font-weight: 500; font-size: 11px; letter-spacing: 9px; margin-top: 8px;
  }
  .back-divider {
    position: absolute; left: 268px; top: 60px; width: 1.5px; height: 190px;
    background: var(--brand-red);
  }
  .back-copy { position: absolute; left: 292px; top: 48px; width: 230px; }
  .mission {
    color: var(--brand-red); font-weight: 700; font-size: 11.5px;
    line-height: 1.35; text-transform: uppercase;
  }
  .mission .lower { text-transform: none; }
  .services { list-style: none; margin-top: 16px; }
  .services li {
    display: flex; align-items: center; gap: 9px;
    font-size: 11.5px; font-weight: 400; line-height: 1.65;
  }
  .services li::before {
    content: ""; width: 7px; height: 7px; background: var(--brand-red);
    transform: rotate(45deg); flex: none;
  }
  .since {
    position: absolute; right: 26px; bottom: 40px; font-size: 11px;
  }

  /* ---------- Front: white side ---------- */
  .card--front { left: 620px; background: var(--card-white); color: var(--ink); }
  .front-brand { position: absolute; right: 36px; top: 34px; text-align: left; }
  .front-brand .brand-name { font-size: 34px; color: var(--ink); }
  .front-brand .brand-sub { font-size: 9.5px; letter-spacing: 7.5px; color: var(--ink); }
  .person { position: absolute; left: 34px; top: 128px; }
  .person-name {
    color: var(--brand-red); font-weight: 700; font-size: 23px; letter-spacing: 0.2px;
  }
  .person-title {
    font-size: 11.5px; font-weight: 500; margin-top: 3px; text-transform: uppercase;
  }
  .rule {
    position: absolute; left: 34px; right: 30px; top: 186px; height: 1.5px;
    background: var(--brand-red);
  }
  .contacts { position: absolute; left: 34px; top: 200px; list-style: none; }
  .contacts li {
    display: flex; align-items: center; gap: 10px;
    font-size: 11.5px; line-height: 1.7;
  }
  .contacts svg { width: 12px; height: 12px; fill: var(--brand-red); flex: none; }
  .location {
    position: absolute; right: 30px; bottom: 34px; font-size: 11.5px; font-weight: 500;
  }
  .front-band { position: absolute; left: 0; bottom: 0; width: 540px; height: 22px; }
</style>
</head>
<body>
<main class="stage">

  <section class="card card--back" aria-label="Card back, black">
    <div class="back-brand">
      <div class="brand-row">
        <span class="brand-name">Velmoro</span>
        <span class="brand-mark"></span>
      </div>
      <div class="brand-sub">CONSULTING</div>
    </div>
    <div class="back-divider"></div>
    <div class="back-copy">
      <p class="mission">As the owner's rep<br>we aim to achieve your<br>infrastructure vision <span class="lower">with</span><br>our specialization <span class="lower">in:</span></p>
      <ul class="services">
        <li>FUNDING Planning</li>
        <li>BUSINESS Planning</li>
        <li>INFRASTRUCTURE Planning</li>
        <li>PROJECT Management</li>
      </ul>
    </div>
    <p class="since">Since 2012</p>
  </section>

  <section class="card card--front" aria-label="Card front, white">
    <div class="front-brand">
      <div class="brand-row">
        <span class="brand-name">Velmoro</span>
        <span class="brand-mark"></span>
      </div>
      <div class="brand-sub">CONSULTING</div>
    </div>
    <div class="person">
      <h1 class="person-name">Marisol Dunbar-Okafor</h1>
      <p class="person-title">CEO / Lead Project Manager</p>
    </div>
    <div class="rule"></div>
    <ul class="contacts">
      <li><svg viewBox="0 0 24 24" aria-hidden="true"><path d="M6.6 10.8a15.1 15.1 0 0 0 6.6 6.6l2.2-2.2a1 1 0 0 1 1-.25 11.4 11.4 0 0 0 3.6.57 1 1 0 0 1 1 1V20a1 1 0 0 1-1 1A17 17 0 0 1 3 4a1 1 0 0 1 1-1h3.5a1 1 0 0 1 1 1c0 1.25.2 2.45.57 3.57a1 1 0 0 1-.25 1z"/></svg>867.555.0192</li>
      <li><svg viewBox="0 0 24 24" aria-hidden="true"><path d="M2 5h20v14H2z M2 5l10 8 10-8" fill="none" stroke="#e3163b" stroke-width="2.4"/></svg>marisol@velmoro.ca</li>
      <li><svg viewBox="0 0 24 24" aria-hidden="true"><circle cx="12" cy="12" r="9.5" fill="none" stroke="#e3163b" stroke-width="2.4"/><path d="M2.5 12h19M12 2.5c3 3 3 16 0 19M12 2.5c-3 3-3 16 0 19" fill="none" stroke="#e3163b" stroke-width="1.8"/></svg>www.velmoro.ca</li>
    </ul>
    <p class="location">Northgate NT · Eastbrook NB</p>
    <svg class="front-band" viewBox="0 0 540 22" preserveAspectRatio="none" aria-hidden="true">
      <polygon points="0,22 0,8 360,8 372,0 372,22" fill="var(--brand-red)"/>
      <polygon points="372,0 540,0 540,22 372,22" fill="var(--ink-soft)"/>
    </svg>
  </section>

</main>
</body>
</html>
```